Revamp our wedding venue website

Currently we are using wordpress for our website and hoped to find a designer that can assist us with making the website prettier and more pleasing and draw more interest. www.velmarhall.com is our current site. We are connected to google business mail, so I would prefer to stay with this for now and update our gallery with new photos, blog page and putting the contact us form back on all the pages.

Target Market(s)

20-40 years of age, all ranges of styles and generally clients looking for a different modern feel vs. a hotel hall.

Industry/Entity Type

Wedding

Logo Text

1927 Velmar Hall

Number of Pages Required

4 page

Font styles to use
Serif

Requirements
Must have
• Light, airy feel. Romantic and informative. Mobile friendly and easy to contact us-preferred contact form on all pages. Gallery of photos. Previous reviews
Nice to have
• Bio of staff, maybe some videos, and fun things to do in the area for out of town guests. Maps and also venue blank floor plan.

```html
<!DOCTYPE html>
<html lang="en">
<head>
<meta charset="utf-8">
<title>1927 Velmar Hall — Weddings &amp; Events</title>
<link href="https://fonts.googleapis.com/css2?family=Open+Sans:wght@400;600;700&family=Playball&display=swap" rel="stylesheet">
<style>
:root{
  --teal:#7ccfcb;
  --teal-dark:#4fb3ae;
  --teal-light:#a9e0dc;
  --orange:#f59a3c;
  --orange-soft:#f7a85a;
  --text:#555;
  --muted:#888;
  --grey-bg:#f4f5f7;
  --white:#fff;
  --dark:#111;
}
*{margin:0;padding:0;box-sizing:border-box}
html,body{width:1200px;height:3020px;overflow:hidden;background:var(--white)}
body{font-family:"Open Sans",Arial,sans-serif;color:var(--text);position:relative}
.script{font-family:"Playball",cursive}
.abs{position:absolute}

/* top bar */
.topbar{top:0;left:0;width:1200px;height:44px;background:linear-gradient(90deg,var(--teal-dark),var(--teal));color:#fff;font-size:12px;display:flex;align-items:center;padding:0 86px}
.topbar span{margin-right:40px}
.topbar .socials{margin-left:auto;display:flex;gap:8px}
.socials i{width:24px;height:24px;border:1.5px solid #fff;border-radius:50%;display:block}

/* header */
.header{top:44px;left:0;width:1200px;height:88px;display:flex;align-items:center;padding:0 86px;border-bottom:1px solid #eee}
.brand{font-family:"Open Sans",Arial,sans-serif;font-weight:700;font-size:24px;color:var(--dark)}
.nav{margin-left:auto;display:flex;gap:34px;font-size:12px;font-weight:600;color:#333}
.nav .active{color:var(--orange)}
.nav-tools{display:flex;gap:10px;margin-left:30px}
.nav-tools i{width:38px;height:38px;border-radius:50%;display:block;border:1.5px solid var(--orange)}
.nav-tools i+i{border-color:var(--teal)}

/* hero */
.hero{top:132px;left:0;width:1200px;height:518px;background:linear-gradient(100deg,#d8d4cf 0%,#ece9e4 35%,#f7f6f3 60%,#fbfbfa 100%)}
.hero-text{position:absolute;right:86px;top:160px;width:370px;text-align:right}
.hero-text h1{font-family:"Playball",cursive;font-weight:400;font-size:38px;color:var(--teal)}
.hero-text h2{font-family:"Playball",cursive;font-weight:400;font-size:21px;color:var(--orange);line-height:1.4;margin-top:6px}
.hero-text p{font-family:"Playball",cursive;font-size:15px;color:#333;line-height:1.7;margin-top:10px}
.dots{display:flex;gap:5px}
.dots i{width:12px;height:12px;border-radius:50%;border:1.5px solid #888;display:block}
.dots i.on{background:var(--orange);border-color:var(--orange)}

/* divider */
.divider{left:450px;width:300px;height:30px}

/* section heading */
.sec-title{left:0;width:1200px;text-align:center;font-family:"Playball",cursive;font-size:32px;color:var(--orange)}
.sec-title em{font-style:normal;color:var(--teal)}
.sec-lead{left:240px;width:720px;text-align:center;font-size:12px;line-height:2}

/* features */
.feature{width:300px;text-align:center}
.feature .ring{width:108px;height:108px;border-radius:50%;border:2px solid var(--orange);margin:0 auto;display:flex;align-items:center;justify-content:center}
.feature.teal .ring{border-color:var(--teal)}
.feature h3{font-family:"Playball",cursive;font-weight:400;font-size:24px;color:var(--orange);margin-top:22px}
.feature.teal h3{color:var(--teal)}
.feature p{font-size:12px;line-height:2;margin-top:10px}

/* video */
.video-band{top:1154px;left:0;width:1200px;height:396px;background:var(--grey-bg)}
.video{left:86px;top:1194px;width:472px;height:310px;background:#5dd3c8}
.video-bar{position:absolute;left:0;bottom:0;width:100%;height:30px;background:#1b1b1b}
.video-bar::before{content:"";position:absolute;left:0;top:0;width:100%;height:4px;background:#c62828}
.play{position:absolute;left:50%;top:50%;width:60px;height:42px;margin:-21px 0 0 -30px;background:#e52d27;border-radius:10px}
.play::after{content:"";position:absolute;left:24px;top:12px;border-left:16px solid #fff;border-top:9px solid transparent;border-bottom:9px solid transparent}
.video-copy{left:608px;top:1164px;width:506px}
.video-copy h2{font-family:"Playball",cursive;font-weight:400;font-size:30px;color:var(--orange);margin-top:56px}
.video-copy p{font-size:12px;line-height:2.05;margin-top:14px}

/* reviews */
.reviews{top:1550px;left:0;width:1200px;height:402px;background:linear-gradient(135deg,var(--orange) 0%,var(--orange-soft) 60%,#f8b574 100%);color:#fff}
.reviews .sec-title{color:#fff}
.review{width:330px;display:flex;gap:16px}
.avatar{width:88px;height:88px;border-radius:50%;border:4px solid #fff;background:linear-gradient(#d9c2ad,#9c7f69);flex:none}
.review p{font-size:12px;line-height:1.9}
.review h4{font-size:11px;font-weight:700;margin-top:22px}
.review small{font-size:10px;display:block;margin-top:2px}
.stars{display:flex;gap:2px;margin-top:4px}

/* gallery */
.gallery{left:86px;top:2148px;width:1028px;height:437px;display:grid;grid-template-columns:repeat(4,1fr);grid-template-rows:1fr 1fr;gap:2px}
.gallery div{background:#333}
.gallery .caption-tile{background:linear-gradient(#f6b26b,#ee9b4c);color:#fff;text-align:center;padding:34px 24px}
.caption-tile h3{font-family:"Playball",cursive;font-weight:400;font-size:22px}
.caption-tile p{font-size:11px;line-height:2;margin-top:8px}
.caption-tile .btns{display:flex;gap:12px;justify-content:center;margin-top:12px}
.caption-tile .btns i{width:28px;height:28px;border-radius:50%;border:1.5px solid #fff;display:block}
.tall{grid-row:span 2}

/* partners */
.partners{top:2616px;left:60px;width:1080px;height:92px;display:flex;align-items:center;justify-content:space-between;font-size:24px;font-weight:600;color:#999}
.partners .arrow{font-size:22px;font-weight:400;color:#aaa}

/* footer */
.footer{top:2708px;left:0;width:1200px;height:312px;background:linear-gradient(180deg,var(--teal-light),var(--teal))}
.footer .brand{color:#fff;position:absolute;left:94px;top:128px;font-size:24px}
.fcol{position:absolute;top:42px;color:#fff;font-size:11px;line-height:1.8}
.fcol h4{font-family:"Playball",cursive;font-weight:400;font-size:22px;margin-bottom:16px}
.fcol li{list-style:none;display:flex;align-items:center;gap:12px;margin-bottom:10px}
.fcol li i{width:12px;height:12px;background:#fff;border-radius:2px;display:block;opacity:.85}
.field{width:240px;height:32px;background:#fff;color:#444;font-size:11px;padding:8px 12px;margin-top:16px}
.subscribe{display:inline-block;background:var(--teal-dark);padding:4px 10px;margin-top:10px;font-size:11px}
.fsocial{display:flex;gap:10px;margin-top:18px}
.fsocial i{width:34px;height:34px;border:1.5px solid #fff;border-radius:50%;display:block}
.copyright{top:2980px;left:0;width:1200px;text-align:center;color:#fff;font-size:12px}
</style>
</head>
<body>

<div class="abs topbar">
  <span>&#9742; Call us : 555.204.1927</span>
  <span>&#9993; Email : events@velmarhall.com</span>
  <div class="socials"><i></i><i></i><i></i><i></i></div>
</div>

<header class="abs header">
  <div class="brand">1927 Velmar Hall</div>
  <nav class="nav">
    <span class="active">HOME</span><span>WEDDINGS</span><span>EVENTS</span><span>CATERING</span><span>GALLERY</span><span>CONTACT US</span>
  </nav>
  <div class="nav-tools"><i></i><i></i></div>
</header>

<section class="abs hero" role="img" aria-label="Photo of a bride and groom embracing under a veil, bride holding a pink bouquet">
  <div class="hero-text">
    <h1>1927 Velmar Hall</h1>
    <h2>Imagine your wedding or event in Bayview's premiere, unique and historic venue</h2>
    <p>Watch this short video to find out more about having your event here at the 1927 Velmar Hall. Then, look around wedding and event specialists today</p>
  </div>
  <div class="dots abs" style="left:562px;top:484px"><i></i><i></i><i class="on"></i><i></i></div>
  <div class="dots abs" style="left:1042px;top:484px"><i></i><i></i><i class="on"></i><i></i></div>
</section>

<!-- intro -->
<svg class="abs divider" style="top:690px" viewBox="0 0 300 30"><line x1="10" y1="15" x2="290" y2="15" stroke="#333" stroke-width="1"/><circle cx="150" cy="15" r="5" fill="none" stroke="#333"/></svg>
<h2 class="abs sec-title" style="top:734px">Weddings &amp; Events at <em>the 1927 Velmar Hall</em></h2>
<p class="abs sec-lead" style="top:790px">When choosing the location for your wedding or event, the 1927 Velmar Hall provides you with an all-inclusive experience, from the bar, serves up wonderful libations and specialty cocktails that enhance your experience.</p>

<div class="abs feature" style="left:102px;top:882px">
  <div class="ring"><svg width="50" height="50" viewBox="0 0 50 50" fill="none" stroke="#f59a3c" stroke-width="4"><circle cx="19" cy="29" r="12"/><circle cx="31" cy="29" r="12"/></svg></div>
  <h3>Weddings</h3>
  <p>When choosing the location for your wedding or event, the 1927 Velmar Hall provides you with an experience, from photo opportunities</p>
</div>
<div class="abs feature teal" style="left:450px;top:882px">
  <div class="ring"><svg width="40" height="40" viewBox="0 0 40 40" fill="none" stroke="#7ccfcb" stroke-width="2.5"><rect x="4" y="7" width="32" height="29" rx="2"/><line x1="4" y1="15" x2="36" y2="15"/><line x1="12" y1="3" x2="12" y2="10"/><line x1="28" y1="3" x2="28" y2="10"/><line x1="14" y1="15" x2="14" y2="36"/><line x1="26" y1="15" x2="26" y2="36"/><line x1="4" y1="25" x2="36" y2="25"/></svg></div>
  <h3>Events</h3>
  <p>When choosing the location for your wedding or event, the 1927 Velmar Hall provides you with an experience, from photo opportunities</p>
</div>
<div class="abs feature" style="left:798px;top:882px">
  <div class="ring"><svg width="52" height="52" viewBox="0 0 52 52" fill="#f59a3c"><circle cx="26" cy="13" r="3"/><path d="M6 34a20 20 0 0 1 40 0z"/><rect x="3" y="36" width="46" height="4" rx="2"/></svg></div>
  <h3>Catering</h3>
  <p>When choosing the location for your wedding or event, the 1927 Velmar Hall provides you with an experience, from photo opportunities</p>
</div>

<!-- video -->
<section class="abs video-band"></section>
<div class="abs video" role="img" aria-label="Video thumbnail for Bright Citrus Films on a teal background">
  <div class="play"></div>
  <div class="video-bar"></div>
</div>
<svg class="abs divider" style="top:1164px;left:660px" viewBox="0 0 300 30"><line x1="10" y1="15" x2="290" y2="15" stroke="#333"/><circle cx="150" cy="15" r="5" fill="none" stroke="#333"/></svg>
<div class="abs video-copy">
  <h2>Weddings Videos</h2>
  <p>When choosing the location for your wedding or event, the 1927 Velmar Hall provides you with an all-inclusive experience, from the moment you arrive, through the creative food, and amazing photo opportunities. The unique open-kitchen provides you, and your guests a front-row seat to our creative, and talented chefs, as they prepare a culinary experience like no other. The full, and spacious bar, serves up wonderful libations and specialty cocktails that enhance your experience.</p>
  <p>The unique open-kitchen provides you, and your guests a front-row seat to our creative, and talented chefs, as they prepare a culinary experience like no other. The full, and spacious bar, serves cocktails that enhance your experience.</p>
</div>

<!-- reviews -->
<section class="abs reviews">
  <svg class="abs divider" style="top:42px" viewBox="0 0 300 30"><line x1="10" y1="15" x2="290" y2="15" stroke="#fff"/><circle cx="150" cy="15" r="5" fill="none" stroke="#fff"/></svg>
  <h2 class="abs sec-title" style="top:88px">Read Our Reviews</h2>
  <p class="abs sec-lead" style="top:132px;color:#fff">When choosing the location for your wedding or event, the 1927 Velmar Hall provides you with an all-inclusive experience</p>

  <div class="abs review" style="left:86px;top:188px">
    <div class="avatar" role="img" aria-label="Reviewer portrait"></div>
    <div><p>&ldquo; My fiance and I are extremely excited to start planning our wedding at this amazing venue! Mara and the rest of the staff have been very...</p><h4>ANA RIVERA</h4><small>POSTED ON 25 OCT 2016</small>
    <svg class="stars" width="70" height="12" viewBox="0 0 70 12" fill="none" stroke="#fff"><path id="st" d="M6 1l1.5 3.3 3.5.4-2.6 2.4.7 3.5L6 8.8 2.9 10.6l.7-3.5L1 4.7l3.5-.4z"/><use href="#st" x="14"/><use href="#st" x="28"/><use href="#st" x="42"/><use href="#st" x="56"/></svg></div>
  </div>
  <div class="abs review" style="left:436px;top:188px">
    <div class="avatar" role="img" aria-label="Reviewer portrait"></div>
    <div><p>&ldquo; My fiance and I are extremely excited to start planning our wedding at this amazing venue! Mara and the rest of the staff have been very...</p><h4>ANA RIVERA</h4><small>POSTED ON 25 OCT 2016</small>
    <svg class="stars" width="70" height="12" viewBox="0 0 70 12" fill="none" stroke="#fff"><use href="#st"/><use href="#st" x="14"/><use href="#st" x="28"/><use href="#st" x="42"/><use href="#st" x="56"/></svg></div>
  </div>
  <div class="abs review" style="left:786px;top:188px">
    <div class="avatar" role="img" aria-label="Reviewer portrait"></div>
    <div><p>&ldquo; My fiance and I are extremely excited to start planning our wedding at this amazing venue! Mara and the rest of the staff have been very...</p><h4>ANA RIVERA</h4><small>POSTED ON 25 OCT 2016</small>
    <svg class="stars" width="70" height="12" viewBox="0 0 70 12" fill="none" stroke="#fff"><use href="#st"/><use href="#st" x="14"/><use href="#st" x="28"/><use href="#st" x="42"/><use href="#st" x="56"/></svg></div>
  </div>
</section>

<!-- gallery -->
<svg class="abs divider" style="top:1982px" viewBox="0 0 300 30"><line x1="10" y1="15" x2="290" y2="15" stroke="#333"/><circle cx="150" cy="15" r="5" fill="none" stroke="#333"/></svg>
<h2 class="abs sec-title" style="top:2026px">Photo <em>Gallery</em></h2>
<p class="abs sec-lead" style="top:2080px">When choosing the location for your wedding or event, the 1927 Velmar Hall provides you with an all-inclusive experience, from the bar, serves up wonderful libations and specialty cocktails that enhance your experience.</p>
<div class="abs gallery">
  <div class="caption-tile">
    <h3>1927 Velmar Hall</h3>
    <p>It is a long established fact that a reader will be distracted by the read more Lorem text to using English.</p>
    <div class="btns"><i></i><i></i></div>
  </div>
  <div class="tall" role="img" aria-label="Bottle in a blue Wedlist sleeve on a bar counter" style="background:linear-gradient(#2a1f1a,#3a6f8f 60%,#1d1714)"></div>
  <div style="grid-column:span 2;background:linear-gradient(#6f8a9a,#b88a8f 55%,#6b6b6b)" role="img" aria-label="Wedding party in pink dresses and grey suits celebrating on a city street"></div>
  <div role="img" aria-label="Bride in a veil on a purple-lit stage" style="background:linear-gradient(#241533,#5b3b7a 60%,#1a1020)"></div>
  <div role="img" aria-label="Model walking a runway at a bridal show" style="background:linear-gradient(#0f2a3a,#3d5a6b 60%,#1a1a1a)"></div>
  <div role="img" aria-label="Group of women smiling at an event" style="background:linear-gradient(#3a2a2a,#8a6a5a 55%,#2a2020)"></div>
</div>

<div class="abs partners">
  <span class="arrow">&lsaquo;</span>
  <span>Soundloop</span><span>Quadrant</span><span>Snapgrid</span><span>framestock</span><span>Tilepay</span><span>Snapgrid</span>
  <span class="arrow">&rsaquo;</span>
</div>

<!-- footer -->
<footer class="abs footer">
  <div class="brand">1927 Velmar Hall</div>
  <div class="fcol" style="left:382px">
    <h4>Contact Us</h4>
    <ul>
      <li><i></i>555.204.1927 (Phone)</li>
      <li><i></i>555.204.1928 (Fax)</li>
      <li><i></i>hello@velmarhall.com</li>
      <li><i></i>1927 Harbor Row, Bayview, FL 30000</li>
    </ul>
  </div>
  <div class="fcol" style="left:628px;width:250px">
    <h4>Newsletters</h4>
    <p>Register Your email address to get information about us</p>
    <div class="field">Email Address</div>
    <span class="subscribe">SUBSCRIBE</span>
  </div>
  <div class="fcol" style="left:906px;width:200px">
    <h4>Follow Us</h4>
    <p>Lorem ipsum dolor sit amet, conse ctetur adipiscing elit. Nulla in purus nibh. Donec ornare</p>
    <div class="fsocial"><i></i><i></i><i></i><i></i><i></i></div>
  </div>
</footer>
<p class="abs copyright">&copy; Copyright 2016 1927 Velmar Hall All Rights Reserved</p>

</body>
</html>
```